Invitation Design Project

In May 2014, my husband and I celebrate our 10th wedding anniversary, and in June 2014 I celebrate my 40th birthday. We will be having a "10/40" party in June 2014 for both events.

This party will be held on my property, "Hollowmere Farm" in North Queensland, so the invitation needs to be fun, whimsical and reflective of both our farm and the Australian bush. You can see photos of our property on facebook: https://www.pagebook.example/hollowmerefarm

The party will be held on 7 June 2014, RSVP by 1 April 2014.

Target Market(s)

Our family and friends - all ages and backgrounds

Industry/Entity Type

Wedding

Requirements
Must have
• Must have the following details: (wording is flexible)
- Mirla & Tobias celebrate their 10th wedding anniversary on 8 May 2014.
- Mirla turns 40 on 9 June 2014
- Party to be held on Hollowmere Farm, 6pm start. Dinner, entertainment and courtesy bus provided, BYO drinks.
- RSVP by 1 April 2014
Must have correct spelling and grammar on the first draft please.
Nice to have
• It might be fun if the invitation could include our pets (dogs, cats, goats, pigs, chickens, parrakeet - see pictures on the facebook link above) in some way, in cartoon form in the background maybe?
Should not have
• I'm not particularly interested in having our photos incorporated into the invitation.

```html
<!DOCTYPE html>
<html lang="en">
<head>
<meta charset="utf-8">
<title>Mirla &amp; Tobias — 10/40 Party Invitation</title>
<link rel="stylesheet" href="https://fonts.googleapis.com/css2?family=Archivo+Black&family=Antonio:wght@100;200&family=Oswald:wght@700&display=swap">
<style>
  :root {
    --ink-black: #000000;
    --bush-mint: #a3f7c6;
    --bush-mint-soft: #7fd9a6;
    --headline-red: #ec2229;
    --glow-white: rgba(255, 255, 255, 0.62);
    --detail-white: #ffffff;
    --party-magenta: #e628d8;
    --byo-gold: #f7b500;
  }
  * { margin: 0; padding: 0; box-sizing: border-box; }
  html, body {
    width: 1200px;
    height: 848px;
    overflow: hidden;
    background: var(--ink-black);
  }
  .invitation {
    position: relative;
    width: 1200px;
    height: 848px;
    background: var(--ink-black);
    overflow: hidden;
  }
  .bush-artwork {
    position: absolute;
    inset: 0;
    width: 1200px;
    height: 848px;
  }
  .headline-panel {
    position: absolute;
    left: 92px;
    top: 30px;
    width: 975px;
    height: 150px;
    background: var(--glow-white);
    box-shadow: 0 0 18px 10px var(--glow-white);
  }
  .headline {
    position: absolute;
    left: 92px;
    top: 34px;
    width: 975px;
    text-align: center;
    font-family: "Archivo Black", "Arial Black", sans-serif;
    font-size: 41px;
    line-height: 51px;
    color: var(--headline-red);
    letter-spacing: 0.5px;
  }
  .headline sup {
    font-size: 22px;
    vertical-align: 16px;
    line-height: 0;
  }
  .event-details {
    position: absolute;
    left: 734px;
    top: 278px;
    font-family: "Antonio", "Arial Narrow", sans-serif;
    font-weight: 100;
    color: var(--detail-white);
    font-size: 46px;
    line-height: 68px;
    letter-spacing: 1px;
    list-style: none;
  }
  .event-extras {
    position: absolute;
    left: 620px;
    top: 512px;
    width: 512px;
    text-align: center;
    font-family: "Antonio", "Arial Narrow", sans-serif;
    font-weight: 200;
    color: var(--detail-white);
    font-size: 29px;
    letter-spacing: 0.6px;
    white-space: nowrap;
  }
  .party-chant {
    position: absolute;
    left: 40px;
    top: 490px;
    font-family: "Antonio", "Arial Narrow", sans-serif;
    font-weight: 100;
    color: var(--party-magenta);
    white-space: nowrap;
    transform: rotate(-5deg);
    transform-origin: left bottom;
  }
  .party-chant span { display: inline-block; margin-right: 6px; }
  .party-chant .p1 { font-size: 64px; }
  .party-chant .p2 { font-size: 52px; }
  .party-chant .p3 { font-size: 42px; }
  .party-chant .p4 { font-size: 32px; }
  .byo-note {
    position: absolute;
    left: 934px;
    top: 636px;
    font-family: "Oswald", "Impact", sans-serif;
    font-weight: 700;
    color: var(--byo-gold);
    font-size: 27px;
    letter-spacing: 0.5px;
  }
  .rsvp-note {
    position: absolute;
    left: 619px;
    top: 780px;
    font-family: "Oswald", "Impact", sans-serif;
    font-weight: 700;
    color: var(--detail-white);
    font-size: 33px;
    letter-spacing: 0.8px;
  }
</style>
</head>
<body>
<main class="invitation">
  <svg class="bush-artwork" viewBox="0 0 1200 848" role="img" aria-label="High-contrast mint and black illustration of an Australian bush tree and farm scene">
    <defs>
      <linearGradient id="bushFade" x1="0" y1="0" x2="1" y2="0">
        <stop offset="0" stop-color="var(--bush-mint)" />
        <stop offset="0.55" stop-color="var(--bush-mint-soft)" />
        <stop offset="1" stop-color="var(--ink-black)" />
      </linearGradient>
    </defs>
    <path d="M0 0 H1200 V205 L1080 190 L600 230 L520 330 L640 600 L560 848 H0 Z" fill="url(#bushFade)" />
  </svg>

  <div class="headline-panel"></div>
  <h1 class="headline">
    Please join us in celebrating<br>
    Mirla &amp; Tobias’s 10<sup>th</sup> Wedding<br>
    Anniversary &amp; Mirla’s 40<sup>th</sup> Birthday!
  </h1>

  <ul class="event-details">
    <li>Place: Hollowmere Farm</li>
    <li>Date: 7 June 2014</li>
    <li>Time: Starts at 6pm</li>
  </ul>
  <p class="event-extras">Dinner, entertainment, &amp; courtesy bus provided</p>

  <p class="party-chant">
    <span class="p1">PARTY</span><span class="p2">PARTY</span><span class="p3">PARTY</span><span class="p4">PARTY</span>
  </p>

  <p class="byo-note">BYO Drinks!</p>
  <p class="rsvp-note">Please RSVP by 1 April 2014</p>
</main>
</body>
</html>
```